依頼詳細
地域の協力店舗様に置いていただいたり、ご紹介いただいたお客様にお渡しするチラシになります。

お客様がこれから数十年で数百万円変わる可能性
その一助を担う弊社への信頼感
全てのサポートを行う安心感

などを出して行けたら幸いでございます。
よろしくお願いいたします。
記載項目
https://pages.torimaru.jp/kanko.jp/web/%E3%83%9B%E3%83%BC%E3%83%A0?authuser=0
サイズ
A4
ページ数
片面
希望イメージ
シンプル 複雑
単色 カラフル
暗い 明るい
日常 高級
遊び心 厳粛
未来的 伝統的
女性的 男性的
希望する色
青系、水色系
納品ファイル
• 高解像度JPG (.jpg)
• イラストレーター形式 (.ai)
• フォトショップ形式 (.psd)
• PNG形式 (.png)
補足説明
最終的に文字などをこちらで編集したいと思っております、よろしくお願いいたします。
簡単なイメージファイルを添付いたしますので、取り入れていただけると幸いでございます。

```html
<!DOCTYPE html>
<html lang="ja">
<head>
<meta charset="UTF-8">
<title>携帯料金 ここまで安くなる!?</title>
<link href="https://fonts.googleapis.com/css2?family=M+PLUS+Rounded+1c:wght@500;700;800&display=swap" rel="stylesheet">
<style>
:root{
  --peach-bg:#fbe3d6;
  --peach-light:#fdf0e8;
  --peach-cell:#f7d6c4;
  --orange:#ef8a3a;
  --orange-deep:#e9742a;
  --ink:#3b3431;
  --ink-soft:#6b5e58;
  --white:#ffffff;
  --mark-blue:#5bb0d8;
  --arrow-yellow:#f2c14a;
}
*{margin:0;padding:0;box-sizing:border-box}
html,body{width:849px;height:1200px;overflow:hidden}
body{font-family:"M PLUS Rounded 1c",sans-serif;color:var(--ink);background:var(--peach-bg)}
.flyer{position:relative;width:849px;height:1200px;background:var(--peach-bg)}
.brand{position:absolute;display:flex;align-items:center;gap:10px}
.brand-dot{width:34px;height:34px;border-radius:50%;background:var(--mark-blue);flex:none}
.brand-name{font-size:26px;font-weight:700;color:var(--ink-soft);line-height:1;white-space:nowrap}
.brand--top{left:28px;top:40px}
.illustration{position:absolute;left:30px;top:120px;width:300px;height:470px;border-radius:20px;
  background:linear-gradient(180deg,#f6c9b2 0%,#f3b293 55%,#f1d37c 100%)}
.badge{position:absolute;left:622px;top:52px;width:168px;height:168px;border-radius:50%;background:var(--orange);
  color:var(--white);font-weight:800;font-size:44px;line-height:1.1;display:flex;align-items:center;justify-content:center;text-align:center}
.headline{position:absolute;left:332px;top:180px;font-weight:800;color:var(--ink);line-height:1.2}
.headline .l1{display:block;font-size:70px}
.headline .l2{display:block;font-size:76px;padding-left:78px;white-space:nowrap}
.headline em{font-style:normal;color:var(--orange);font-size:92px}
.checklist{position:absolute;left:430px;top:415px;width:370px;height:160px;background:var(--white);border-radius:16px;
  border:2px dashed var(--orange);padding:38px 24px 0 34px}
.checklist-title{position:absolute;left:50%;top:-20px;transform:translateX(-50%);background:var(--white);
  color:var(--orange);font-weight:800;font-size:22px;padding:0 10px;white-space:nowrap}
.checklist li{list-style:none;display:flex;align-items:center;gap:10px;font-weight:700;font-size:21px;margin-bottom:10px}
.tick{width:22px;height:22px;border-radius:4px;background:var(--orange);display:flex;align-items:center;justify-content:center;flex:none}
.plan{position:absolute;left:92px;top:642px;width:668px;border-collapse:collapse;font-weight:700}
.plan caption{background:var(--orange);color:var(--white);font-size:28px;height:50px;line-height:50px;text-align:center}
.plan td{height:52px;font-size:24px;border-bottom:3px solid var(--peach-bg)}
.plan .who{background:var(--peach-cell);color:var(--ink-soft);padding-left:18px;width:150px;font-weight:500}
.plan .before{background:var(--white);color:var(--ink-soft);text-align:center;width:230px}
.plan .arrow{background:var(--white);width:50px;text-align:center}
.plan .after{background:var(--peach-light);color:var(--orange-deep);text-align:right;padding-right:40px;font-size:28px;font-weight:800}
.saving{position:absolute;left:92px;top:935px;width:668px;height:62px;background:var(--orange);color:var(--white);
  font-weight:800;font-size:38px;text-align:center;line-height:62px;border-radius:4px}
.cta{position:absolute;left:0;top:1010px;width:849px;text-align:center;color:var(--orange-deep);font-weight:800;font-size:30px}
.footer{position:absolute;left:0;top:1062px;width:849px;height:138px;background:var(--white)}
.brand--foot{left:40px;top:52px}
.contacts{position:absolute;left:280px;top:18px;list-style:none}
.contacts li{display:flex;align-items:center;gap:12px;font-size:14px;font-weight:500;height:34px;color:var(--ink)}
.contacts .ic{width:24px;height:24px;border-radius:50%;background:var(--orange);display:flex;align-items:center;justify-content:center;flex:none}
</style>
</head>
<body>
<main class="flyer">
  <div class="brand brand--top"><div class="brand-dot"></div><span class="brand-name">ことりまる</span></div>
  <div class="illustration" role="img" aria-label="スマートフォンを持つ女性のイラスト"></div>
  <div class="badge">携帯<br>料金</div>
  <h1 class="headline"><span class="l1">ここまで</span><span class="l2">安くなる<em>!?</em></span></h1>

  <section class="checklist">
    <p class="checklist-title">全てお任せください!</p>
    <ul>
      <li><span class="tick"><svg width="14" height="14" viewBox="0 0 14 14"><path d="M2 7l3 3 7-7" fill="none" stroke="#fff" stroke-width="2.5"/></svg></span>携帯料金の見直し</li>
      <li><span class="tick"><svg width="14" height="14" viewBox="0 0 14 14"><path d="M2 7l3 3 7-7" fill="none" stroke="#fff" stroke-width="2.5"/></svg></span>面倒なデータ移行</li>
      <li><span class="tick"><svg width="14" height="14" viewBox="0 0 14 14"><path d="M2 7l3 3 7-7" fill="none" stroke="#fff" stroke-width="2.5"/></svg></span>その他引き継ぎ設定</li>
    </ul>
  </section>

  <table class="plan">
    <caption>例) Aさん家族の場合</caption>
    <tr><td class="who">お父さま</td><td class="before">8,900 円</td><td class="arrow"><svg width="20" height="26" viewBox="0 0 20 26"><path d="M2 2l16 11L2 24z" fill="#f2c14a"/></svg></td><td class="after">1,390 円</td></tr>
    <tr><td class="who">お母さま</td><td class="before">8,900 円</td><td class="arrow"><svg width="20" height="26" viewBox="0 0 20 26"><path d="M2 2l16 11L2 24z" fill="#f2c14a"/></svg></td><td class="after">290 円</td></tr>
    <tr><td class="who">お子さま</td><td class="before">8,900 円</td><td class="arrow"><svg width="20" height="26" viewBox="0 0 20 26"><path d="M2 2l16 11L2 24z" fill="#f2c14a"/></svg></td><td class="after">290 円</td></tr>
    <tr><td class="who">お子さま</td><td class="before">8,900 円</td><td class="arrow"><svg width="20" height="26" viewBox="0 0 20 26"><path d="M2 2l16 11L2 24z" fill="#f2c14a"/></svg></td><td class="after">290 円</td></tr>
  </table>

  <p class="saving">年間 244,800 円の節約に!</p>
  <p class="cta">▼詳しくはこちらからご相談ください▼</p>

  <footer class="footer">
    <div class="brand brand--foot"><div class="brand-dot"></div><span class="brand-name">ことりまる</span></div>
    <ul class="contacts">
      <li><span class="ic"><svg width="14" height="14" viewBox="0 0 14 14"><path d="M3 1l2 3-1.5 1.5a7 7 0 0 0 5 5L10 9l3 2-1 2c-5 0-11-6-11-11z" fill="#fff"/></svg></span>000-0000-0000</li>
      <li><span class="ic"><svg width="14" height="14" viewBox="0 0 14 14"><circle cx="7" cy="7" r="5.5" fill="none" stroke="#fff" stroke-width="1.4"/><path d="M1.5 7h11M7 1.5c-3 3-3 8 0 11M7 1.5c3 3 3 8 0 11" fill="none" stroke="#fff" stroke-width="1.2"/></svg></span>https://pages.torimaru.jp/kanko.jp/web/ ホーム</li>
      <li><span class="ic"><svg width="14" height="14" viewBox="0 0 14 14"><circle cx="7" cy="7" r="5.5" fill="none" stroke="#fff" stroke-width="1.4"/><path d="M1.5 7h11M7 1.5c-3 3-3 8 0 11M7 1.5c3 3 3 8 0 11" fill="none" stroke="#fff" stroke-width="1.2"/></svg></span>https://pages.torimaru.jp/kanko.jp/web/ お問合わせ</li>
    </ul>
  </footer>
</main>
</body>
</html>
```